Postcard Design

Income tax servicesOver 20 years experienceBusiness and Personal Tax ReturnsAll State ReturnsFree Electronic FilingI would like a simple map showing how to get to my house.reasons to use a tax preparerYou don’t have to keep up with the many tax law changes or understand complicated tax law.Your time is worth money – add up the hours you would spend doing it yourself and calculate what that’s worth.A tax program in a box cannot represent you in an audit.A tax professional can answer your questions to help you make smarter tax-saving decisions.It gives you peace of mind knowing that a professional is taking care of it.It can save you money – if your tax preparer finds even one significant deduction or tax credit you may have missed, it can easily cover the cost to have them prepared.Going to be targeting the area within 2 square miles of my home office so would like to promote proximity to the possible clients

```html
<!DOCTYPE html>
<html lang="en">
<head>
<meta charset="utf-8">
<title>Tax Preparer Postcard</title>
<link href="https://fonts.googleapis.com/css2?family=Oswald:wght@500&family=Lato:wght@400;700;900&family=Roboto:wght@400&display=swap" rel="stylesheet">
<style>
  :root {
    --blue: #1aa6e4;
    --blue-deep: #0d8fd0;
    --blue-light: #5cc6f2;
    --dark: #2d2d2f;
    --ink: #3a3a3c;
    --white: #ffffff;
    --backdrop: #d6d6d6;
    --map: #e6e3dc;
  }
  * { box-sizing: border-box; margin: 0; padding: 0; }
  html, body { width: 806px; height: 1200px; overflow: hidden; }
  body { background: var(--backdrop); position: relative; font-family: 'Lato', sans-serif; }

  .card {
    position: absolute; left: 41px; width: 676px; height: 485px;
    transform: scale(1.072); transform-origin: top left;
    background: var(--white); overflow: hidden;
    box-shadow: 0 2px 6px rgba(0,0,0,.25);
  }
  .card--front { top: 59px; }
  .card--back { top: 622px; height: 484px; }
  .card__shapes { position: absolute; inset: 0; width: 100%; height: 100%; }
  .abs { position: absolute; white-space: nowrap; }

  .headline__main { left: 17px; top: 20px; font-family: 'Oswald', sans-serif; font-weight: 500; font-size: 42px; line-height: 1; color: var(--ink); }
  .headline__sub { left: 17px; top: 76px; font-family: 'Roboto', sans-serif; font-size: 31px; line-height: 1; color: var(--blue); }

  .benefits__title { left: 17px; top: 139px; font-family: 'Oswald', sans-serif; font-weight: 500; font-size: 21px; color: var(--ink); }
  .benefits__list { left: 18px; top: 181px; list-style: none; color: var(--white); font-weight: 700; font-size: 14px; line-height: 17.5px; }
  .benefits__list li::before, .reasons__list li::before { content: ""; display: inline-block; width: 6px; height: 6px; border-radius: 50%; background: currentColor; margin-right: 9px; vertical-align: middle; }

  .call { left: 17px; top: 285px; font-weight: 900; font-size: 26px; color: var(--blue-deep); }
  .call__number { color: var(--ink); margin-left: 4px; }

  .brand { left: 440px; top: 290px; width: 236px; text-align: center; }
  .brand__name { font-weight: 900; font-size: 29px; color: #111; display: inline-flex; align-items: center; gap: 8px; }
  .brand__dot { width: 12px; height: 12px; border-radius: 50%; background: #111; display: inline-block; }
  .brand__tagline { margin-top: 14px; font-family: 'Roboto', sans-serif; font-size: 10px; color: #222; }

  .contact { color: var(--white); font-weight: 700; font-size: 14px; line-height: 22px; }
  .contact__item { display: flex; align-items: center; gap: 7px; }
  .contact__item svg { width: 9px; height: 9px; fill: var(--blue-light); }
  .contact--front { left: 477px; top: 425px; }
  .contact--back { left: 20px; top: 451px; display: flex; gap: 10px; }

  .reasons__title { left: 21px; top: 10px; font-family: 'Oswald', sans-serif; font-weight: 500; font-size: 27px; line-height: 1.1; color: var(--blue-deep); }
  .reasons__sub { left: 21px; top: 44px; font-family: 'Roboto', sans-serif; font-size: 22px; line-height: 1; color: var(--ink); }
  .reasons__list { left: 22px; top: 84px; width: 286px; white-space: normal; list-style: none; color: var(--white); font-weight: 700; font-size: 11.5px; line-height: 14.5px; text-align: justify; hyphens: auto; }
  .reasons__list li { margin-bottom: 14px; padding-left: 13px; text-indent: -13px; }
  .reasons__list li::before { width: 5px; height: 5px; margin-right: 8px; }

  .stamp { left: 552px; top: 28px; width: 62px; height: 86px; border: 1px solid #777; }
</style>
</head>
<body>

<section class="card card--front">
  <svg class="card__shapes" viewBox="0 0 676 485" preserveAspectRatio="none" aria-hidden="true">
    <defs>
      <linearGradient id="panelBlue" x1="0" y1="0" x2="1" y2="1">
        <stop offset="0" stop-color="#35b6ee"/><stop offset="1" stop-color="#0e8fd3"/>
      </linearGradient>
      <linearGradient id="tabGrey" x1="0" y1="0" x2="0" y2="1">
        <stop offset="0" stop-color="#ffffff"/><stop offset="1" stop-color="#d8d8d8"/>
      </linearGradient>
    </defs>
    <polygon points="240,0 262,0 382,265 360,265" fill="var(--blue)"/>
    <polygon points="375,250 676,250 676,265 382,265" fill="var(--blue)"/>
    <polygon points="0,123 285,123 457,455 441,455 275,133 0,133" fill="var(--dark)"/>
    <polygon points="0,133 275,133 441,455 0,455" fill="url(#panelBlue)"/>
    <polygon points="0,135 132,135 122,166 0,166" fill="url(#tabGrey)"/>
    <polygon points="0,278 325,278 310,328 0,328" fill="url(#tabGrey)"/>
    <polygon points="0,455 457,455 470,485 0,485" fill="var(--dark)"/>
    <polygon points="452,412 676,412 676,485 488,485" fill="var(--dark)"/>
  </svg>

  <svg class="abs" style="left:262px;top:0;width:414px;height:250px" viewBox="0 0 414 250" preserveAspectRatio="none" role="img" aria-label="Photo of a businessman in a suit stacking coins into rising columns">
    <defs><linearGradient id="photoTone" x1="0" y1="0" x2="1" y2="1"><stop offset="0" stop-color="#4a4e56"/><stop offset="1" stop-color="#1f2126"/></linearGradient></defs>
    <polygon points="0,0 414,0 414,250 113,250" fill="url(#photoTone)"/>
  </svg>

  <svg class="abs" style="left:0;top:357px;width:292px;height:70px" viewBox="0 0 292 70" preserveAspectRatio="none" role="img" aria-label="Street map showing the office location">
    <polygon points="0,0 292,0 270,70 0,70" fill="var(--map)"/>
  </svg>

  <h1 class="abs headline__main">THE ULTIMATE</h1>
  <p class="abs headline__sub">TAX PREPARER</p>

  <h2 class="abs benefits__title">BENEFITS</h2>
  <ul class="abs benefits__list">
    <li>Over 20 years experience</li>
    <li>Business and Personal Tax Returns</li>
    <li>All State Returns</li>
    <li>Free Electronic Filing</li>
  </ul>

  <p class="abs call">Call now <span class="call__number">123-456-789</span></p>

  <div class="abs brand">
    <div class="brand__name"><span class="brand__dot"></span>Brightline Tax</div>
    <p class="brand__tagline">Brightline Tax. Clear Returns, Close to Home.</p>
  </div>

  <div class="abs contact contact--front">
    <p class="contact__item"><svg viewBox="0 0 10 8"><path d="M0 0h10v8H0z"/></svg>info@loremipsum.com</p>
    <p class="contact__item"><svg viewBox="0 0 10 10"><circle cx="5" cy="5" r="5"/></svg>www.loremipsum.com</p>
  </div>
</section>

<section class="card card--back">
  <svg class="card__shapes" viewBox="0 0 676 484" preserveAspectRatio="none" aria-hidden="true">
    <defs>
      <linearGradient id="backBlue" x1="0" y1="0" x2="1" y2="1">
        <stop offset="0" stop-color="#38b8ef"/><stop offset="1" stop-color="#0e8fd3"/>
      </linearGradient>
      <linearGradient id="backTab" x1="0" y1="0" x2="0" y2="1">
        <stop offset="0" stop-color="#ffffff"/><stop offset="1" stop-color="#d6d6d6"/>
      </linearGradient>
    </defs>
    <polygon points="0,0 385,0 338,440 0,440" fill="url(#backBlue)"/>
    <polygon points="250,0 394,0 347,440 335,440 380,18 250,18" fill="var(--dark)"/>
    <polygon points="0,0 252,0 232,75 0,75" fill="url(#backTab)"/>
    <polygon points="0,440 352,440 352,484 0,484" fill="var(--dark)"/>
  </svg>

  <h2 class="abs reasons__title">REASONS TO USE</h2>
  <p class="abs reasons__sub">A TAX PREPARER</p>

  <ul class="abs reasons__list">
    <li>You don’t have to keep up with the many tax law changes or understand complicated tax law.</li>
    <li>Your time is worth money – add up the hours you would spend doing it yourself and calculate what that’s worth.</li>
    <li>A tax program in a box cannot represent you in an audit.</li>
    <li>A tax professional can answer your questions to help you make smarter tax-saving decisions.</li>
    <li>It gives you peace of mind knowing that a professional is taking care of it.</li>
    <li>It can save you money – if your tax preparer finds even one significant deduction or tax credit you may have missed, it can easily cover the cost to have them prepared.</li>
    <li>Going to be targeting the area within 2 square miles of my home office so would like to promote proximity to the possible clients</li>
  </ul>

  <div class="abs contact contact--back">
    <p class="contact__item"><svg viewBox="0 0 10 8"><path d="M0 0h10v8H0z"/></svg>info@loremipsum.com</p>
    <p class="contact__item"><svg viewBox="0 0 10 10"><circle cx="5" cy="5" r="5"/></svg>www.loremipsum.com</p>
  </div>

  <div class="abs stamp"></div>
</section>

</body>
</html>
```